Banner Ad in Spanish for Car Accident Law Firm in Miami Florida

I need a Banner Ad in Spanish Language. We are an Accident Law Firm in Miami, FL. We help injured people. I need a Banner Ad with a Vibrant Colorful Background to Stand Out. A Click-Able Call to Action is needed. We don't want to make the banner too crowded and we want the message to be simple to understand. We are looking for a skilled graphic designer to create a visually appealing banner ad for our YouTube marketing campaign. The required dimensions and format are:
1920 x 275
.png & .mp4

The Banner is for our Plaintiff’s Personal Injury Law Firm. We represent Spanish Speaking clients who are injured in CAR ACCIDENTS. As such the banner must include:
1. Our Firm Logo
2. Our Telephone# (305) 471-6023
3. Stock Photo of Car Crash
4. Photo of our attorney in office
5. The Words Abogados de Accidentes
The telephone number should be fairly large and stand out it is our call to action. The words Abogados de Accidentes should be close to our Logo to associate the two.

Target Market(s)

Car Accident Victims who speak Spanish

Industry/Entity Type

Legal, Law Firm.

Font styles to use
Sans Serif

Colors
59FF00
82FF00
B8FF75
E3FFCB
F4FFEA
F0912C
F2A743
F7CA91
FBE8D2
FDF5EE
6B429C
8869AF
B7A5CE
E3DAEB
F3F0F8

Requirements
Must have
• A bold background so that Banner Ad can be seen on mobile and against the screen being advertising against
Should not have
• Be too crowded. Hard to understand what it is for.

```html
<!DOCTYPE html>
<html lang="es">
<head>
<meta charset="utf-8">
<title>Marlowe Law Firm – Abogados de Accidentes</title>
<link href="https://fonts.googleapis.com/css2?family=Montserrat:wght@300;700;800&display=swap" rel="stylesheet">
<style>
  :root {
    --page-bg: #1a1b1d;
    --purple: #7a2bd0;
    --magenta: #c02f8c;
    --red: #f2413a;
    --orange-red: #ff4d12;
    --orange: #ff8200;
    --orange-light: #ff9a10;
    --green: #8fcb2f;
    --green-light: #a6d93c;
    --white: #ffffff;
    --ink: #111111;
    --photo-steel: #8d99a6;
    --photo-shadow: #3d4650;
    --suit-grey: #9aa2ab;
  }
  html, body {
    margin: 0;
    width: 1200px;
    height: 1200px;
    overflow: hidden;
    background: var(--page-bg);
    font-family: "Montserrat", Arial, sans-serif;
  }
  .banner {
    position: absolute;
    left: 53px;
    top: 521px;
    width: 1094px;
    height: 157px;
    overflow: hidden;
  }
  .banner-shapes {
    position: absolute;
    inset: 0;
  }
  .brand {
    position: absolute;
    left: 28px;
    top: 50px;
    display: flex;
    align-items: center;
    gap: 10px;
    color: var(--white);
  }
  .brand-mark {
    width: 56px;
    height: 56px;
    background: var(--white);
    border-radius: 6px;
  }
  .brand-name {
    font-weight: 700;
    font-size: 19px;
    line-height: 1.1;
    letter-spacing: 0.5px;
  }
  .headline {
    position: absolute;
    left: 252px;
    top: 14px;
    width: 345px;
    margin: 0;
    text-align: center;
    color: var(--white);
    line-height: 1;
  }
  .headline-strong {
    display: block;
    font-weight: 800;
    font-size: 38px;
    letter-spacing: 0.3px;
  }
  .headline-light {
    display: block;
    font-weight: 300;
    font-size: 38px;
    margin-top: 1px;
  }
  .call-button {
    position: absolute;
    left: 254px;
    top: 93px;
    width: 345px;
    height: 41px;
    border-radius: 5px;
    background: linear-gradient(180deg, var(--green-light), var(--green));
    box-shadow: 0 6px 8px -4px rgba(0,0,0,0.35);
    color: var(--ink);
    font-weight: 800;
    font-size: 33px;
    line-height: 41px;
    text-align: center;
    text-decoration: none;
    letter-spacing: -0.3px;
  }
</style>
</head>
<body>
  <div class="banner">
    <svg class="banner-shapes" width="1094" height="157" viewBox="0 0 1094 157" xmlns="http://www.w3.org/2000/svg">
      <defs>
        <linearGradient id="bg-sweep" x1="0" y1="0" x2="1" y2="0">
          <stop offset="0" stop-color="var(--purple)"/>
          <stop offset="0.3" stop-color="var(--magenta)"/>
          <stop offset="0.47" stop-color="var(--red)"/>
          <stop offset="0.6" stop-color="var(--orange-red)"/>
        </linearGradient>
        <linearGradient id="crash-tones" x1="0" y1="0" x2="1" y2="1">
          <stop offset="0" stop-color="#e4e8ec"/>
          <stop offset="0.45" stop-color="var(--photo-steel)"/>
          <stop offset="1" stop-color="var(--photo-shadow)"/>
        </linearGradient>
        <linearGradient id="portrait-tones" x1="0" y1="0" x2="0" y2="1">
          <stop offset="0" stop-color="var(--orange)"/>
          <stop offset="0.55" stop-color="var(--orange-light)"/>
          <stop offset="1" stop-color="var(--suit-grey)"/>
        </linearGradient>
      </defs>
      <rect class="bg" width="1094" height="157" fill="url(#bg-sweep)"/>
      <rect class="bg-orange" x="880" width="214" height="157" fill="var(--orange)"/>
      <polygon class="accent-green-left" points="636,157 664,157 652,66" fill="var(--green)"/>
      <polygon class="accent-green-right" points="874,0 914,0 896,58" fill="var(--green)"/>
      <polygon class="crash-photo" role="img" aria-label="Foto de un coche plateado con la parte delantera destrozada tras un accidente" points="624,0 876,0 918,157 664,157" fill="url(#crash-tones)"/>
      <rect class="attorney-photo" role="img" aria-label="Foto del abogado con traje gris y corbata en su oficina" x="914" y="0" width="180" height="157" fill="url(#portrait-tones)"/>
    </svg>

    <div class="brand">
      <span class="brand-mark" aria-hidden="true"></span>
      <span class="brand-name">MARLOWE<br>LAW FIRM</span>
    </div>

    <h1 class="headline">
      <span class="headline-strong">ABOGADOS DE</span>
      <span class="headline-light">ACCIDENTES</span>
    </h1>

    <a class="call-button" href="tel:+13054716023">(305) 471-6023</a>
  </div>
</body>
</html>
```